New Home-Based Bakery Needs an Eye-catching Menu/Flavor List Design for Print and Website

We need a menu/flavor list design for our new start-up home-based bake shop called, Copperkettle Bake Shop. The menu will be sent to Zib for printing, but must be in PDF format so we can use it on our site also. This should contain our logo, contact info, website, social media, etc. The design should be professional. Cupcakes on one side/page, and macarons and cookies/brownies on the other.
The artwork must either fit into a 120mm x 120mm (4.72" x 4.72") size frame (preferred) or a 215.9mm x 93.13mm (8.5" x 3.67") size.
The menu should also be landscape, not portrait.
I have attached multiple examples below.
File 1 is our logo. We love the logo that was designed for us! We primarily use the one in the top right corner; but, we like the one underneath it as secondary also.
Files 2, 3, 4, 5, 6, and 7 (landscape orientation) are some examples of how we want this card/menu to look
Files 8 and 9 (portrait orientation) are an example of what someone else did, that we really do not like. It looks too cluttered, not elegant, etc.
File 10 contains our menu list, pricing, and additional info about what we want on the design etc.
Target Market(s)
Anyone who enjoys gourmet baked goods
Industry/Entity Type
Shop
Look and feel

```html
<!DOCTYPE html>
<html lang="en">
<head>
<meta charset="utf-8">
<title>Copperkettle Bake Shop – Cupcake Menu</title>
<link rel="stylesheet" href="https://fonts.googleapis.com/css2?family=Montserrat:wght@700;800&family=Source+Sans+3:wght@400;600;700&display=swap">
<style>
:root{
  --plum-deep:#46205f;
  --plum-bar:#7a5a89;
  --cream:#f7eedc;
  --ink:#2b2230;
  --price-grey:#5a5560;
  --white:#ffffff;
}
*{box-sizing:border-box;margin:0;padding:0}
html,body{width:1200px;height:1200px;overflow:hidden}
body{font-family:"Source Sans 3",sans-serif;color:var(--ink);background:var(--plum-deep)}
.menu{position:relative;width:1200px;height:1200px;background:var(--plum-deep)}
.masthead{position:absolute;left:0;top:0;width:1200px;height:128px;background:var(--plum-deep);color:var(--white)}
.contact-list{position:absolute;left:26px;top:26px;list-style:none;font-size:14px;line-height:20.5px}
.contact-list li{display:flex;align-items:center;gap:12px}
.contact-dot{width:12px;height:12px;border-radius:50%;background:var(--white);flex:none}
.masthead-title{position:absolute;left:0;right:0;top:36px;text-align:center;font-family:"Montserrat",sans-serif;font-weight:800;font-size:54px;letter-spacing:1px}
.brand{position:absolute;right:26px;top:20px;width:190px;text-align:center;font-weight:700;font-size:19px;line-height:21px;letter-spacing:1px}
.brand-mark{display:block;width:48px;height:48px;border-radius:50%;border:2px solid var(--white);margin:0 auto 8px}
.sheet{position:absolute;left:8px;top:128px;width:1184px;height:998px;background:var(--cream)}
.section-head{position:absolute;left:26px;top:24px;display:flex;align-items:baseline;gap:30px}
.section-title{font-weight:700;font-size:62px;color:var(--plum-deep);line-height:1}
.price-list{font-weight:600;font-size:22px;color:var(--price-grey);word-spacing:2px}
.price-list .sep{margin:0 8px}
.flavours{position:absolute;left:18px;top:106px;width:1150px;display:grid;grid-template-columns:repeat(4,265px);column-gap:26px;grid-template-rows:repeat(10,86.4px);grid-auto-flow:column}
.flavour{overflow:hidden}
.flavour-name{background:var(--plum-bar);color:var(--white);font-weight:600;font-size:18px;line-height:25px;height:25px;padding-left:8px;white-space:nowrap}
.flavour-desc{font-size:12.4px;line-height:15.4px;text-align:justify;padding:6px 2px 0 3px;max-height:53px;overflow:hidden}
.footnote{position:absolute;left:0;top:1126px;width:1200px;height:74px;display:flex;align-items:center;justify-content:center;padding:0 60px;text-align:center;color:var(--white);font-style:italic;font-size:17px;line-height:25px}
</style>
</head>
<body>
<main class="menu">
  <header class="masthead">
    <ul class="contact-list">
      <li><span class="contact-dot"></span>www.copperkettlebakeshop.com</li>
      <li><span class="contact-dot"></span>facebook.com/copperkettlebakeshop</li>
      <li><span class="contact-dot"></span>@copperkettlebake</li>
      <li><span class="contact-dot"></span>@copperkettlebakeshop</li>
    </ul>
    <h1 class="masthead-title">MENU</h1>
    <div class="brand"><span class="brand-mark"></span>COPPERKETTLE BAKE SHOP</div>
  </header>

  <section class="sheet">
    <div class="section-head">
      <h2 class="section-title">Cupcakes</h2>
      <p class="price-list">$2.75 each<span class="sep">|</span>$16.00 half dozen<span class="sep">|</span>$30.00 dozen</p>
    </div>

    <div class="flavours">
      <article class="flavour"><h3 class="flavour-name">Banana Peanut Butter</h3><p class="flavour-desc">Fresh banana cupcake topped with creamy peanut butter frosting</p></article>
      <article class="flavour"><h3 class="flavour-name">Bananas Foster</h3><p class="flavour-desc">Caramelized, fresh banana cupcake, infused with rum, topped with caramel buttercream frosting</p></article>
      <article class="flavour"><h3 class="flavour-name">Banana Split</h3><p class="flavour-desc">Fresh banana cupcake, filled with a liquid fudge core, topped with vanilla cream cheese frosting, caramel drizzle, rainbow sprinkles, and a cherry</p></article>
      <article class="flavour"><h3 class="flavour-name">Black and White</h3><p class="flavour-desc">Classic chocolate cupcake topped with vanilla buttercream frosting and rainbow sprinkles</p></article>
      <article class="flavour"><h3 class="flavour-name">Boston Cream</h3><p class="flavour-desc">Classic vanilla cupcake, filled with rich Boston-style pastry cream, dipped in chocolate ganache</p></article>
      <article class="flavour"><h3 class="flavour-name">Carrot</h3><p class="flavour-desc">Cinnamon cupcake, baked with fresh carrots and pecans, topped with vanilla cream cheese frosting</p></article>
      <article class="flavour"><h3 class="flavour-name">Chocolate Butterscotch Chip</h3><p class="flavour-desc">Classic chocolate cupcake, baked with butterscotch chips, topped with butterscotch-infused buttercream frosting</p></article>
      <article class="flavour"><h3 class="flavour-name">Chocolate Coconut</h3><p class="flavour-desc">Classic chocolate cupcake topped with vanilla cream cheese frosting and shredded coconut</p></article>
      <article class="flavour"><h3 class="flavour-name">Chocolate Hazelnut</h3><p class="flavour-desc">Classic chocolate cupcake, baked with toasted hazelnuts, topped with hazelnut-infused chocolate buttercream frosting</p></article>
      <article class="flavour"><h3 class="flavour-name">Chocolate Lava</h3><p class="flavour-desc">Classic chocolate cupcake, filled with a liquid fudge core, topped with vanilla cream cheese frosting and fudge drizzle</p></article>

      <article class="flavour"><h3 class="flavour-name">Chocolate Peanut Butter Chip*</h3><p class="flavour-desc">Classic chocolate cupcake, baked with peanut butter chips, topped with creamy peanut butter frosting</p></article>
      <article class="flavour"><h3 class="flavour-name">Chocolate Salted Caramel</h3><p class="flavour-desc">Classic chocolate cupcake, baked with swirls of caramel sauce, topped with salted caramel buttercream frosting and caramel drizzle</p></article>
      <article class="flavour"><h3 class="flavour-name">Chocolate Strawberry</h3><p class="flavour-desc">Classic chocolate cupcake, baked with fresh strawberries, topped with strawberry buttercream frosting</p></article>
      <article class="flavour"><h3 class="flavour-name">Cinnamon Chip</h3><p class="flavour-desc">Cinnamon cupcake, baked with cinnamon chips, topped with cinnamon buttercream frosting</p></article>
      <article class="flavour"><h3 class="flavour-name">Coconut</h3><p class="flavour-desc">Classic vanilla cupcake topped with vanilla cream cheese frosting and shredded coconut</p></article>
      <article class="flavour"><h3 class="flavour-name">Coffee Mud Fudge</h3><p class="flavour-desc">Classic chocolate cupcake, baked with cream-filled chocolate sandwich cookie crumbles, topped with coffee-infused buttercream and</p></article>
      <article class="flavour"><h3 class="flavour-name">Cookies and Cream</h3><p class="flavour-desc">Classic vanilla cupcake, baked with cream-filled chocolate sandwich cookie crumbles, topped with cream-filled chocolate sandwich cookie</p></article>
      <article class="flavour"><h3 class="flavour-name">Double Chocolate**</h3><p class="flavour-desc">Classic chocolate cupcake topped with whipped chocolate ganache frosting</p></article>
      <article class="flavour"><h3 class="flavour-name">Double Vanilla**</h3><p class="flavour-desc">Classic vanilla cupcake topped with vanilla buttercream frosting</p></article>
      <article class="flavour"><h3 class="flavour-name">German Chocolate</h3><p class="flavour-desc">Classic chocolate cupcake filled and topped with traditional coconut pecan frosting</p></article>

      <article class="flavour"><h3 class="flavour-name">Honey Banana Cinnamon</h3><p class="flavour-desc">Fresh banana cupcake topped with honey-infused cinnamon cream cheese frosting</p></article>
      <article class="flavour"><h3 class="flavour-name">Key Lime</h3><p class="flavour-desc">Fresh key lime cupcake topped with key lime-infused cream cheese frosting</p></article>
      <article class="flavour"><h3 class="flavour-name">Lemon</h3><p class="flavour-desc">Fresh lemon cupcake topped with lemon-infused cream cheese frosting</p></article>
      <article class="flavour"><h3 class="flavour-name">Maple Bacon Cinnamon</h3><p class="flavour-desc">Cinnamon cupcake, baked with real crispy bacon pieces, topped with maple-infused cream cheese frosting</p></article>
      <article class="flavour"><h3 class="flavour-name">Maple Nut</h3><p class="flavour-desc">Maple-infused cupcake, baked with walnuts, topped with maple-infused cream cheese frosting and walnuts</p></article>
      <article class="flavour"><h3 class="flavour-name">Mint Cookie Crunch</h3><p class="flavour-desc">Classic chocolate cupcake, baked with mint cream-filled sandwich cookie crumbles, topped with chocolate ganache and mint cream-filled</p></article>
      <article class="flavour"><h3 class="flavour-name">Mocha</h3><p class="flavour-desc">Classic chocolate cupcake topped with coffee-infused buttercream frosting and a chocolate covered espresso bean</p></article>
      <article class="flavour"><h3 class="flavour-name">Orange Cream</h3><p class="flavour-desc">Fresh orange cupcake topped with vanilla cream cheese frosting</p></article>
      <article class="flavour"><h3 class="flavour-name">Peanut Butter Crunch</h3><p class="flavour-desc">Classic vanilla cupcake, baked with crunchy peanut butter chocolate bar bits, topped with crunchy peanut butter bar buttercream frosting</p></article>
      <article class="flavour"><h3 class="flavour-name">Pineapple Brown Sugar</h3><p class="flavour-desc">Fresh pineapple cupcake topped with brown sugar-infused buttercream frosting and a cherry</p></article>

      <article class="flavour"><h3 class="flavour-name">Red Velvet**</h3><p class="flavour-desc">Classic cupcake, baked with a hint of cocoa and all natural food coloring, topped with vanilla cream cheese frosting</p></article>
      <article class="flavour"><h3 class="flavour-name">S'mores</h3><p class="flavour-desc">Classic chocolate cupcake, filled with a toasted marshmallow core, topped with chocolate ganache and graham cracker crumbs</p></article>
      <article class="flavour"><h3 class="flavour-name">Salted Caramel</h3><p class="flavour-desc">Classic vanilla cupcake, baked with swirls of caramel sauce, topped with salted caramel buttercream frosting and caramel drizzle</p></article>
      <article class="flavour"><h3 class="flavour-name">Strawberry</h3><p class="flavour-desc">Classic vanilla cupcake, baked with fresh strawberries, topped with strawberry buttercream frosting</p></article>
      <article class="flavour"><h3 class="flavour-name">Vanilla Chocolate</h3><p class="flavour-desc">Classic vanilla cupcake topped with whipped chocolate ganache frosting</p></article>
      <article class="flavour"><h3 class="flavour-name">Vanilla Milk Chocolate</h3><p class="flavour-desc">Classic vanilla cupcake topped with milk chocolate buttercream frosting and rainbow sprinkles</p></article>
      <article class="flavour"><h3 class="flavour-name">White Chocolate Raspberry</h3><p class="flavour-desc">Classic vanilla cupcake, baked with fresh raspberries and white chocolate chips, topped with white chocolate-infused cream cheese frosting</p></article>
    </div>
  </section>

  <footer class="footnote">
    <p>Copperkettle Bake Shop only uses prime ingredients such as European butter, pure cane sugar, Belgian chocolate, French cocoa, cage-free eggs, organic dairy, Madagascar bourbon vanilla, minimally processed US-grown flour, fresh organic produce, and name brand mix-ins.</p>
  </footer>
</main>
</body>
</html>
```